R. Calloway Peril Counsel Business Card

I need a business card that incorporates a two divisions of my company into one business card. The main company or division is R. Calloway Peril Counsel. We have a secondary division of R. Calloway Peril Counsel call Calloway Haulage Cover. I would like this name to be listed as "A Division of R. Calloway Peril Counsel".

Target Market(s)

Customers looking for insurance for their business. WE target businesses with revenues over $5MM

Industry/Entity Type

Business Insurance

Contact Information for Business Card

Use the current logo, but make the R. Calloway Peril Counsel most prevelant over the Calloway Haulage Cover. Name, email, phone number and location

Colors
0054AA
0677BA
7BADD7
CADEEF
E8F1F8

Requirements
Must have
• my current logo
Nice to have
• would like to have "A Division of R. Calloway Peril Counsel" on the card

```html
<!DOCTYPE html>
<html lang="en">
<head>
<meta charset="utf-8">
<title>R. Calloway Peril Counsel – Business Card</title>
<link rel="stylesheet" href="https://fonts.googleapis.com/css2?family=Cinzel:wght@500;600&family=Montserrat:wght@400;500&display=swap">
<style>
  :root {
    --page-bg: #2a2a2d;
    --card-navy: #1d1c45;
    --ink: #e6e8ef;
    --ink-soft: #cfd2dc;
    --rule: #8e91a8;
    --tab-light: #d9dadf;
    --tab-dark: #8f9097;
  }
  * { margin: 0; padding: 0; box-sizing: border-box; }
  html, body { width: 1200px; height: 900px; overflow: hidden; }
  body { background: var(--page-bg); position: relative; font-family: "Montserrat", sans-serif; color: var(--ink); }

  .card {
    position: absolute; left: 100px; top: 165px;
    width: 1000px; height: 570px;
    background: var(--card-navy);
    border-radius: 34px;
    overflow: hidden;
  }
  .edge-tab {
    position: absolute; left: 0; top: 132px; width: 11px; height: 46px;
    background: linear-gradient(90deg, var(--tab-dark), var(--tab-light));
  }

  .brand-mark {
    position: absolute; left: 56px; top: 40px; width: 78px; height: 78px;
    border: 3px solid var(--ink);
  }
  .brand-name {
    position: absolute; left: 152px; top: 60px;
    font-family: "Cinzel", serif; font-weight: 600; font-size: 37px;
    letter-spacing: 1px; color: var(--ink); white-space: nowrap;
  }
  .brand-rule { position: absolute; left: 820px; right: 0; top: 108px; height: 1px; background: var(--rule); }

  .person-name {
    position: absolute; left: 56px; top: 140px;
    font-family: "Cinzel", serif; font-weight: 600; font-size: 30px; letter-spacing: 1px;
  }
  .person-role { position: absolute; left: 56px; top: 182px; font-size: 17px; color: var(--ink-soft); }

  .contact { position: absolute; display: flex; align-items: center; gap: 12px; font-size: 18px; letter-spacing: 0.3px; white-space: nowrap; }
  .contact svg { width: 15px; height: 15px; flex: none; fill: var(--ink-soft); }

  .rule { position: absolute; height: 1px; background: var(--rule); }

  .division-name {
    position: absolute; right: 60px; top: 402px;
    font-family: "Cinzel", serif; font-weight: 600; font-size: 34px; letter-spacing: 1px;
    color: var(--ink); white-space: nowrap;
  }
  .division-note {
    position: absolute; right: 60px; top: 452px;
    font-family: "Cinzel", serif; font-weight: 500; font-size: 15px; letter-spacing: 1.5px;
    color: var(--ink-soft); white-space: nowrap;
  }
</style>
</head>
<body>
  <svg width="0" height="0" style="position:absolute">
    <symbol id="icon-phone" viewBox="0 0 16 16"><path d="M3 1h3l1.5 4-2 1.2a9 9 0 0 0 4.3 4.3L11 8.5l4 1.5v3a2 2 0 0 1-2 2A12 12 0 0 1 1 3a2 2 0 0 1 2-2z"/></symbol>
    <symbol id="icon-mail" viewBox="0 0 16 16"><path d="M1 3h14v10H1z M2 4l6 5 6-5" /></symbol>
    <symbol id="icon-globe" viewBox="0 0 16 16"><circle cx="8" cy="8" r="7"/></symbol>
  </svg>

  <main class="card">
    <div class="edge-tab"></div>

    <div class="brand-mark"></div>
    <div class="brand-name">R. Calloway Peril Counsel</div>
    <div class="brand-rule"></div>

    <div class="person-name">Dana Merrow</div>
    <div class="person-role">Founder / CEO</div>

    <div class="contact" style="left:56px; top:218px;"><svg><use href="#icon-phone"/></svg>404-555-0187</div>
    <div class="contact" style="left:56px; top:248px;"><svg><use href="#icon-mail"/></svg>Dana@RCallowayCounsel.com</div>

    <div class="rule" style="left:56px; width:400px; top:292px;"></div>

    <div class="contact" style="left:56px; top:312px;"><svg><use href="#icon-phone"/></svg>770-555-0142 Haulage Main</div>
    <div class="contact" style="left:56px; top:344px;"><svg><use href="#icon-globe"/></svg>www.CallowayHaulageCover.com</div>

    <div class="contact" style="left:560px; top:300px;"><svg><use href="#icon-phone"/></svg>770-555-0198 R. Calloway Main</div>
    <div class="contact" style="left:560px; top:332px;"><svg><use href="#icon-globe"/></svg>www.RCallowayPerilCounsel.com</div>
    <div class="rule" style="left:560px; right:60px; top:376px;"></div>

    <div class="division-name">Calloway Haulage Cover</div>
    <div class="division-note">A Division of R. Calloway Peril Counsel</div>
  </main>
</body>
</html>
```